Building certification business in Sydney Australia

Brookvale Assessors is a small business that is currently growing and needs a profession looking website to attract customers and give them all the information they need. The main services we offer currently are pre-purchase building inspections for purchasers and other areas of construction consultancy including pool fencing certificates. Please see attached logos to incorporate to also match colour schemes with. Thanks!

Target Market(s)

Prospective buyers and home owners

Industry/Entity Type

Small Business

Requirements
Must have
• Promote the main services from the home page. Being able to select the type of service/certificate required from the main page and be directed to a specific page that deals with only that service containing the relevant information for that item.
Nice to have
• Small emphasis on the location of our office and areas we service etc.

```html
<!DOCTYPE html>
<html lang="en">
<head>
<meta charset="utf-8">
<title>Brookvale Assessors – Building Certification</title>
<link href="https://fonts.googleapis.com/css2?family=Noto+Serif:wght@400;700&family=Open+Sans:wght@400;600&display=swap" rel="stylesheet">
<style>
  :root {
    --header-teal: #087ea4;
    --nav-blue: #14b1e0;
    --brand-ink: #1f5f86;
    --white: #ffffff;
    --text-dark: #222222;
    --text-muted: #555555;
    --rule: #e4e4e4;
    --panel-dark: #363d44;
    --panel-edge: #23282d;
    --field-text: #9a9a9a;
    --accent: #1aa3d9;
    --photo-a: #7d7466;
    --photo-b: #a69a86;
    --photo-c: #6b7d4a;
  }
  * { box-sizing: border-box; margin: 0; padding: 0; }
  html, body { width: 1200px; height: 684px; overflow: hidden; background: var(--white); }
  body { position: relative; font-family: "Noto Serif", serif; color: var(--text-dark); }

  .site-header { position: absolute; left: 0; top: 0; width: 1200px; height: 65px; background: var(--header-teal); }
  .brand {
    position: absolute; left: 109px; top: 0; width: 302px; height: 50px; background: var(--white);
    display: flex; align-items: center; gap: 12px; padding: 0 14px;
  }
  .brand-mark { width: 28px; height: 28px; background: var(--brand-ink); border-radius: 4px; flex: none; }
  .brand-name { font-family: "Open Sans", sans-serif; font-weight: 600; font-size: 22px; color: var(--brand-ink); white-space: nowrap; }

  .main-nav { position: absolute; left: 0; top: 65px; width: 1200px; height: 41px; background: var(--nav-blue); }
  .main-nav ul { list-style: none; position: absolute; left: 109px; top: 0; display: flex; height: 41px; }
  .main-nav li {
    font-size: 13px; letter-spacing: 1px; color: var(--white); padding: 0 16px;
    line-height: 41px; border-right: 1px solid rgba(255,255,255,0.35);
  }
  .main-nav li:last-child { border-right: none; }
  .main-nav li.is-active {
    background: var(--white); color: var(--header-teal); width: 105px; text-align: center;
    margin-top: -4px; line-height: 45px; height: 45px; border-radius: 2px 2px 0 0; padding: 0;
  }

  .intro { position: absolute; left: 109px; top: 138px; width: 984px; text-align: center; }
  .intro h1 { font-weight: 400; font-size: 25px; line-height: 34px; color: var(--text-dark); }
  .intro p { margin-top: 13px; font-size: 17px; color: var(--text-muted); }
  .intro-rule { position: absolute; left: 109px; top: 235px; width: 984px; height: 1px; background: var(--rule); }

  .hero-frame { position: absolute; left: 109px; top: 261px; width: 628px; height: 318px; border: 1px solid #dcdcdc; padding: 4px; }
  .hero-photo {
    width: 100%; height: 100%;
    background: linear-gradient(100deg, var(--photo-c) 0%, var(--photo-a) 35%, var(--photo-b) 70%, #c9c2b6 100%);
  }

  .services-head { position: absolute; left: 109px; top: 596px; width: 628px; }
  .services-head h2 { font-weight: 400; font-size: 19px; }
  .slider-controls { position: absolute; right: 4px; top: 4px; display: flex; gap: 7px; }
  .slider-controls svg { width: 24px; height: 24px; display: block; }
  .services-rule { position: absolute; left: 109px; top: 641px; width: 628px; height: 1px; background: var(--rule); }
  .service-list { position: absolute; left: 109px; top: 661px; width: 640px; display: flex; list-style: none; }
  .service-list li { width: 217px; font-size: 17px; color: var(--text-dark); }

  .booking {
    position: absolute; left: 779px; top: 261px; width: 312px; height: 440px;
    background: var(--panel-dark); border: 2px solid var(--panel-edge); border-radius: 5px;
    font-family: "Open Sans", sans-serif; color: var(--white);
  }
  .booking-handle {
    position: absolute; left: 104px; top: 22px; width: 104px; height: 13px; border-radius: 7px;
    background: #1b1f23; border: 2px solid #6d747a;
  }
  .booking h3, .booking h4 { position: absolute; left: 0; width: 100%; text-align: center; font-weight: 400; font-size: 16px; }
  .booking h3 { top: 55px; }
  .booking h4 { top: 251px; }
  .field {
    position: absolute; left: 26px; width: 253px; height: 36px; background: var(--white);
    border-radius: 4px; box-shadow: inset 0 2px 3px rgba(0,0,0,0.25);
    font-size: 11px; color: var(--field-text); padding: 10px 12px;
  }
  .field.select { left: 25px; width: 250px; font-size: 12px; }
  .field.select::after {
    content: ""; position: absolute; right: 12px; top: 15px;
    border-left: 4px solid transparent; border-right: 4px solid transparent; border-top: 4px solid #444;
  }
</style>
</head>
<body>
  <header class="site-header">
    <div class="brand">
      <span class="brand-mark"></span>
      <span class="brand-name">Brookvale Assessors</span>
    </div>
  </header>

  <nav class="main-nav">
    <ul>
      <li class="is-active">HOME</li>
      <li>ABOUT</li>
      <li>SERVICES</li>
      <li>CONTACT</li>
    </ul>
  </nav>

  <section class="intro">
    <h1>Trusted and Reliable Building Certification</h1>
    <p>With a commitment to client satisfaction and quality certification, why not book us now?</p>
  </section>
  <div class="intro-rule"></div>

  <figure class="hero-frame">
    <div class="hero-photo" role="img" aria-label="Builder in hard hat and high-visibility vest measuring timber formwork on a site"></div>
  </figure>

  <section class="services-head">
    <h2>Our Services</h2>
    <div class="slider-controls">
      <svg viewBox="0 0 24 24" aria-label="Previous"><circle cx="12" cy="12" r="12" fill="var(--accent)"/><path d="M14 7 L9 12 L14 17" stroke="#fff" stroke-width="2.6" fill="none" stroke-linecap="round" stroke-linejoin="round"/></svg>
      <svg viewBox="0 0 24 24" aria-label="Pause"><circle cx="12" cy="12" r="12" fill="var(--accent)"/><rect x="8.5" y="7.5" width="2.4" height="9" fill="#fff"/><rect x="13.1" y="7.5" width="2.4" height="9" fill="#fff"/></svg>
      <svg viewBox="0 0 24 24" aria-label="Next"><circle cx="12" cy="12" r="12" fill="var(--accent)"/><path d="M10 7 L15 12 L10 17" stroke="#fff" stroke-width="2.6" fill="none" stroke-linecap="round" stroke-linejoin="round"/></svg>
    </div>
  </section>
  <div class="services-rule"></div>
  <ul class="service-list">
    <li>Pre-Purchase Inspection</li>
    <li>Pool Certification</li>
    <li>Building Consultancy</li>
  </ul>

  <aside class="booking">
    <div class="booking-handle"></div>
    <h3>Book an Appointment Online</h3>
    <div class="field" style="top:101px">Name</div>
    <div class="field" style="top:152px">Email</div>
    <div class="field" style="top:203px">Contact Number</div>
    <h4>Select Date and Time</h4>
    <div class="field select" style="top:295px">Select Service</div>
    <div class="field" style="top:353px; left:26px; width:253px; font-size:12px">Select Date</div>
    <div class="field select" style="top:402px">Select Time</div>
  </aside>
</body>
</html>
```